The Pipe Lantern business cards

Hi
i have attached a photo, this is how i want the front of my business card to look like:
i want the water drop on the right to be orange
and the water drop on the left to be gloss black
"The" and "Pty Ltd." will be in the same orange as the water drop
and "Pipe Lantern" will be in white
The background of the logo will be a matte black
on the back of the business card i need the following info:
'The Pipe Lantern pty ltd. '
'Plumbing . Drainage . Gas Fitting . Roofing . Jet Blasting . CCTV . '
Also my contact details:
Cal Yardley
0418672913
thepipelantern@mailkestrel.com
Licence# 583016K
Target Market(s)
Strata managers, building managers, the general public
Industry/Entity Type
Business

```html
<!DOCTYPE html>
<html lang="en">
<head>
<meta charset="utf-8">
<title>The Pipe Lantern business cards</title>
<link rel="stylesheet" href="https://fonts.googleapis.com/css2?family=Nunito:wght@800&family=Arimo:wght@400;700&display=swap">
<style>
  :root {
    --page-bg: #e6e7ea;
    --matte-black: #1d1d1f;
    --matte-black-soft: #2c2c2f;
    --brand-orange: #f07a1a;
    --text-white: #ffffff;
    --text-soft: #c9c9cc;
    --card-white: #f5f6f7;
    --wave-pale: #e2e2e5;
    --wave-mid: #c4c4c8;
    --ink: #222225;
  }
  * { box-sizing: border-box; margin: 0; padding: 0; }
  html, body { width: 1200px; height: 900px; overflow: hidden; }
  body {
    background: var(--page-bg);
    font-family: "Arimo", Arial, sans-serif;
    position: relative;
  }
  .card {
    position: absolute;
    width: 660px;
    height: 377px;
    border-radius: 4px;
    overflow: hidden;
    box-shadow: 0 6px 18px rgba(0,0,0,0.15);
  }

  /* Back card */
  .card-back {
    left: 60px; top: 50px;
    background: linear-gradient(150deg, var(--matte-black) 0%, var(--matte-black-soft) 100%);
    text-align: center;
  }
  .card-back .brand-line {
    position: absolute; left: 0; right: 0; top: 110px;
    display: flex; justify-content: center; align-items: center; gap: 12px;
  }
  .brand-dot {
    width: 18px; height: 18px; border-radius: 50%;
    background: var(--brand-orange); flex: none;
  }
  .card-back .brand {
    font-family: "Nunito", Arial, sans-serif;
    font-weight: 800; font-size: 34px; color: var(--text-white);
  }
  .card-back .services {
    position: absolute; left: 0; right: 0; top: 172px;
    font-size: 18px; line-height: 1.45; color: var(--brand-orange);
  }
  .card-back .licence {
    position: absolute; left: 0; right: 0; top: 300px;
    font-size: 14px; color: var(--text-soft);
  }

  /* Front card */
  .card-front {
    left: 60px; top: 470px;
    background: var(--card-white);
  }
  .card-front .waves { position: absolute; inset: 0; }
  .card-front .logo-block {
    position: absolute; left: 40px; top: 150px; width: 300px;
  }
  .card-front .brand-line { display: flex; align-items: flex-start; gap: 10px; }
  .card-front .brand-dot { margin-top: 8px; }
  .card-front .brand {
    font-family: "Nunito", Arial, sans-serif;
    font-weight: 800; font-size: 26px; line-height: 1.15; color: var(--matte-black);
  }
  .card-front .services {
    margin-top: 10px; margin-left: 28px;
    font-size: 14px; line-height: 1.45; color: var(--brand-orange); font-weight: 700;
  }
  .contact {
    position: absolute; left: 370px; top: 80px;
  }
  .contact .person {
    font-family: "Nunito", Arial, sans-serif;
    font-weight: 800; font-size: 28px; color: var(--matte-black);
    margin-bottom: 18px;
  }
  .contact .line {
    display: flex; align-items: center; gap: 10px;
    font-size: 15px; color: var(--ink); margin-bottom: 8px;
  }
  .contact .line svg { flex: none; }

  /* Logo panel */
  .logo-panel {
    position: absolute; left: 780px; top: 560px;
    width: 360px; height: 200px;
    background: var(--matte-black);
    display: flex; align-items: center; justify-content: center; gap: 16px;
  }
  .logo-panel .brand-dot { width: 26px; height: 26px; }
  .logo-panel .brand {
    width: 250px;
    font-family: "Nunito", Arial, sans-serif;
    font-weight: 800; font-size: 30px; line-height: 1.15; color: var(--text-white);
  }
</style>
</head>
<body>

  <section class="card card-back" aria-label="Business card back">
    <div class="brand-line">
      <span class="brand-dot"></span>
      <span class="brand">The Pipe Lantern pty ltd.</span>
    </div>
    <div class="services">Plumbing • Drainage • Gas Fitting<br>Roofing • Jet Blasting • CCTV</div>
    <div class="licence">Licence # 583016K</div>
  </section>

  <section class="card card-front" aria-label="Business card front">
    <svg class="waves" width="660" height="377" viewBox="0 0 660 377" aria-hidden="true">
      <path d="M0 0 H300 C220 20 120 60 0 90 Z" fill="var(--wave-pale)"/>
      <path d="M0 0 H170 C110 25 60 40 0 55 Z" fill="var(--wave-mid)"/>
      <path d="M0 377 V300 C200 330 420 300 660 190 V377 Z" fill="var(--wave-pale)"/>
      <path d="M0 377 V335 C230 350 450 320 660 240 V377 Z" fill="var(--wave-mid)"/>
      <path d="M120 377 C330 370 500 340 660 290 V377 Z" fill="var(--matte-black)"/>
    </svg>
    <div class="logo-block">
      <div class="brand-line">
        <span class="brand-dot"></span>
        <span class="brand">The Pipe Lantern pty ltd.</span>
      </div>
      <div class="services">Plumbing • Drainage • Gas Fitting<br>Roofing • Jet Blasting • CCTV</div>
    </div>
    <div class="contact">
      <div class="person">Cal Yardley</div>
      <div class="line">
        <svg width="12" height="18" viewBox="0 0 12 18" aria-hidden="true">
          <rect x="1" y="1" width="10" height="16" rx="2" fill="none" stroke="var(--brand-orange)" stroke-width="2"/>
          <circle cx="6" cy="14" r="1.2" fill="var(--brand-orange)"/>
        </svg>
        <span>0418672913</span>
      </div>
      <div class="line">
        <svg width="18" height="13" viewBox="0 0 18 13" aria-hidden="true">
          <rect x="0" y="0" width="18" height="13" rx="1" fill="var(--brand-orange)"/>
          <path d="M1 1 L9 7 L17 1" fill="none" stroke="#ffffff" stroke-width="1.5"/>
        </svg>
        <span>thepipelantern@mailkestrel.com</span>
      </div>
    </div>
  </section>

  <section class="logo-panel" aria-label="Logo">
    <span class="brand-dot"></span>
    <span class="brand">The Pipe Lantern pty ltd.</span>
  </section>

</body>
</html>
```